Biz Cards for Velmora Associates

Velmora Associates is seeking a single-sided business card that is more visually-appealing than our current design (see attached).

Notes:
- Our colors are blue & teal.
- Our tag line must be large enough to be easily read
- We don't necessarily need our address included (that's just the biz office)
- We'd like to add our email address: Velmora417@quillbox.net

Thanks!

Industry/Entity Type

Business

Contact Information for Business Card

Standard size
PSD file required w/ text on its own layer

Colors
86cfc6
3277b5

```html
<!DOCTYPE html>
<html lang="en">
<head>
<meta charset="utf-8">
<title>Velmora Associates – Business Card</title>
<link href="https://fonts.googleapis.com/css2?family=Montserrat:wght@300;400;500;700&family=Open+Sans:ital,wght@1,400&display=swap" rel="stylesheet">
<style>
  :root {
    --brand-blue: #1a75bb;
    --brand-teal: #4fc1c5;
    --ink: #231f20;
    --paper: #ffffff;
    --page: #ffffff;
  }
  * { margin: 0; padding: 0; box-sizing: border-box; }
  html, body {
    width: 1200px; height: 1000px; overflow: hidden;
    background: var(--page);
    font-family: "Montserrat", Arial, sans-serif;
  }
  .card {
    position: absolute; left: 259px; top: 295px;
    width: 683px; height: 411px;
    background: var(--paper);
    border: 2px solid var(--brand-blue);
    overflow: hidden;
  }
  .card__waves { position: absolute; left: 0; top: 0; width: 100%; height: 100%; }
  .brand {
    position: absolute; left: 0; right: 0; top: 18px;
    text-align: center;
  }
  .brand__dot {
    display: block; margin: 0 auto;
    width: 96px; height: 96px; border-radius: 50%;
    border: 2px solid var(--ink);
  }
  .brand__name {
    margin-top: 6px;
    font-weight: 500; font-size: 38px; letter-spacing: 1px;
    color: var(--ink); line-height: 1.1;
  }
  .brand__tagline {
    position: absolute; left: 0; right: 0; top: 183px;
    text-align: center;
    font-family: "Open Sans", Arial, sans-serif;
    font-style: italic; font-size: 11px;
    color: var(--brand-blue);
  }
  .person {
    position: absolute; left: 29px; top: 246px; color: var(--paper);
  }
  .person__name { font-weight: 700; font-size: 22px; line-height: 28px; }
  .person__role { font-weight: 300; font-size: 19px; line-height: 26px; }
  .divider {
    position: absolute; left: 313px; top: 236px;
    width: 1px; height: 107px; background: var(--paper);
  }
  .contacts {
    position: absolute; left: 341px; top: 238px;
    list-style: none; color: var(--paper);
    font-weight: 300; font-size: 19px; line-height: 25.5px;
  }
  .contacts b { font-weight: 700; display: inline-block; width: 33px; }
  .address {
    position: absolute; left: 0; right: 0; top: 364px;
    text-align: center; color: var(--paper);
    font-weight: 300; font-size: 19px;
  }
</style>
</head>
<body>
  <div class="card">
    <svg class="card__waves" viewBox="0 0 683 411" preserveAspectRatio="none" aria-hidden="true">
      <path d="M0 163 Q341 250 683 163 L683 411 L0 411 Z" fill="var(--brand-teal)"/>
      <path d="M0 187 Q341 246 683 187 L683 411 L0 411 Z" fill="var(--brand-blue)"/>
    </svg>

    <div class="brand">
      <span class="brand__dot"></span>
      <div class="brand__name">Velmora Associates</div>
    </div>
    <p class="brand__tagline">Thoughtful Care. Steady Minds. Kind Support.</p>

    <div class="person">
      <p class="person__name">Dana Whitcombe, RN</p>
      <p class="person__role">Mental Health Therapist</p>
    </div>

    <span class="divider"></span>

    <ul class="contacts">
      <li><b>P:</b>(855) 555-0142</li>
      <li><b>F:</b>(330) 555-0187</li>
      <li><b>E:</b>Velmora417@quillbox.net</li>
      <li>www.VelmoraAssoc.net</li>
    </ul>

    <p class="address">4120 Alder Ridge Rd Suite 310 Brookfield, OH&nbsp; 44403</p>
  </div>
</body>
</html>
```